Eastlane Holdings Card

I would like a modern, eye catching card based off my logo design.
Info to include:
Tomas Velden (Card Name)
eastlaneholdings.com (Website)
555 283 6091 (Office/fax)
555 736 2840 (Business Cell)
tomas@eastlaneholdings.com (Work email)

Target Market(s)

Commercial real estate brokers, property owners.

Colors
ec1f27
757575

Requirements
Must have
• Name and info above. Not be lame!:)

```html
<!DOCTYPE html>
<html lang="en">
<head>
<meta charset="utf-8">
<title>Eastlane Holdings Card</title>
<link href="https://fonts.googleapis.com/css2?family=Montserrat:wght@500;600;700&family=Work+Sans:wght@400&display=swap" rel="stylesheet">
<style>
  :root {
    --bg: #3b332f;
    --card: #1d1d1e;
    --card-edge: #8e1a1f;
    --red: #ec1f27;
    --red-deep: #c41c23;
    --white: #f4f4f4;
    --grey: #757575;
  }
  html, body {
    margin: 0;
    padding: 0;
    width: 1200px;
    height: 715px;
    overflow: hidden;
    background: var(--bg);
  }
  .canvas {
    position: relative;
    width: 1200px;
    height: 715px;
  }
  .card {
    position: absolute;
    width: 500px;
    height: 286px;
    background: var(--card);
    border-radius: 4px;
    box-shadow: 0 10px 24px rgba(0,0,0,.45);
    box-sizing: border-box;
  }
  .card--front {
    left: 60px;
    top: 214px;
    border-bottom: 4px solid var(--card-edge);
    display: flex;
    align-items: center;
    justify-content: center;
  }
  .card--back {
    left: 640px;
    top: 214px;
  }

  /* Front wordmark */
  .wordmark {
    text-align: center;
    font-family: "Montserrat", sans-serif;
  }
  .wordmark__mark {
    width: 34px;
    height: 34px;
    background: var(--red);
    margin: 0 auto 16px;
  }
  .wordmark__name {
    color: var(--red);
    font-weight: 700;
    font-size: 26px;
    letter-spacing: .5px;
    text-transform: uppercase;
    line-height: 1;
  }
  .tagline {
    display: flex;
    align-items: center;
    justify-content: center;
    gap: 10px;
    margin-top: 8px;
    color: var(--white);
    font-family: "Montserrat", sans-serif;
    font-weight: 600;
    font-size: 10px;
    letter-spacing: 2.4px;
    text-transform: uppercase;
  }
  .tagline::before, .tagline::after {
    content: "";
    width: 34px;
    height: 1.5px;
    background: var(--white);
  }

  /* Back */
  .back__brand {
    position: absolute;
    left: 28px;
    top: 0;
    width: 180px;
    height: 100%;
    display: flex;
    flex-direction: column;
    justify-content: center;
    font-family: "Montserrat", sans-serif;
    font-weight: 700;
    font-size: 30px;
    line-height: 1.05;
    color: var(--white);
    text-transform: uppercase;
  }
  .back__divider {
    position: absolute;
    left: 222px;
    top: 44px;
    width: 2px;
    height: 198px;
    background: var(--red-deep);
  }
  .back__info {
    position: absolute;
    left: 244px;
    top: 40px;
    right: 20px;
  }
  .back__company {
    font-family: "Montserrat", sans-serif;
    font-weight: 700;
    font-size: 15px;
    color: var(--red);
    text-transform: uppercase;
    letter-spacing: .4px;
  }
  .back__info .tagline {
    justify-content: flex-start;
    font-size: 7px;
    letter-spacing: 1.6px;
    margin-top: 4px;
  }
  .back__info .tagline::before, .back__info .tagline::after { width: 20px; height: 1px; }
  .person__name {
    margin-top: 14px;
    font-family: "Montserrat", sans-serif;
    font-weight: 500;
    font-size: 24px;
    letter-spacing: 2px;
    color: var(--red);
    text-transform: uppercase;
  }
  .person__role {
    font-family: "Work Sans", sans-serif;
    font-size: 13px;
    color: var(--white);
    margin-top: 2px;
  }
  .contacts {
    list-style: none;
    margin: 14px 0 0;
    padding: 0;
    font-family: "Work Sans", sans-serif;
    font-size: 14px;
    color: var(--white);
  }
  .contacts li {
    display: flex;
    align-items: center;
    gap: 8px;
    line-height: 20px;
  }
  .contacts svg { width: 10px; height: 10px; fill: var(--red); flex: none; }
</style>
</head>
<body>
<main class="canvas">
  <section class="card card--front">
    <div class="wordmark">
      <div class="wordmark__mark"></div>
      <div class="wordmark__name">Eastlane Holdings</div>
      <div class="tagline">Construction &amp; Roofing</div>
    </div>
  </section>

  <section class="card card--back">
    <div class="back__brand"><span>Eastlane</span><span>Holdings</span></div>
    <div class="back__divider"></div>
    <div class="back__info">
      <div class="back__company">Eastlane Holdings</div>
      <div class="tagline">Construction &amp; Roofing</div>
      <div class="person__name">Tomas Velden</div>
      <div class="person__role">Founder</div>
      <ul class="contacts">
        <li><svg viewBox="0 0 10 10"><path d="M2 0.5l2 2-1 1.2c.6 1.3 1.5 2.2 2.8 2.8l1.2-1 2 2-1.3 1.8C4.5 9 1 5.5.5 1.8z"/></svg>555 283 6091</li>
        <li><svg viewBox="0 0 10 10"><path d="M2.5 0h5v10h-5zM3.5 1.2v6.6h3V1.2z"/></svg>555 736 2840</li>
        <li><svg viewBox="0 0 10 10"><path d="M0 2h10v6H0zM1 3v.3l4 2.5 4-2.5V3L5 5.4z"/></svg>tomas@eastlaneholdings.com</li>
        <li><svg viewBox="0 0 10 10"><circle cx="5" cy="5" r="5"/></svg>eastlaneholdings.com</li>
      </ul>
    </div>
  </section>
</main>
</body>
</html>
```